We are growing our coaching practice and need some help creating collateral

Our organisation is building a coaching practice. It's going well and we want to take it to the next level. To date, we've done our own basic marketing material (attached), but now we want to create something more substantial that captures our approach and gives us confidence and pride when talking to customers. Things to note - we aren't looking for logo design, that's a separate branding discussion in our organisation. We are looking for someone to take our existing content and make it look good - this might be in the form of a flyer or PPT slide deck for example.
The format we are looking for is the offering title - in this case, 'Coaching', a brief description, and then some further detail.
Target Market(s)
Corporate, Healthcare, IT
Colors
Designer to choose colors to be used in the design.
Look and feel
Each slider illustrates characteristics of the customer's brand and the style your logo design should communicate.

```html
<!DOCTYPE html>
<html lang="en">
<head>
<meta charset="utf-8">
<title>Northvale Executive Coaching</title>
<link rel="stylesheet" href="https://fonts.googleapis.com/css2?family=Source+Sans+3:wght@400;600;700&display=swap">
<style>
  :root{
    --charcoal:#5f6062;
    --charcoal-dark:#58595b;
    --mist:#dcdcde;
    --orange:#f07122;
    --ink:#2f2f30;
    --white:#ffffff;
    --wordmark-grey:#6b6b6d;
  }
  *{margin:0;padding:0;box-sizing:border-box;}
  html,body{width:928px;height:1200px;overflow:hidden;background:var(--white);}
  body{font-family:"Source Sans 3",sans-serif;color:var(--ink);}
  .flyer{position:relative;width:928px;height:1200px;overflow:hidden;background:var(--white);}
  .backdrop{position:absolute;left:0;top:0;width:928px;height:1200px;}
  .abs{position:absolute;}

  .hero-title{left:41px;top:34px;font-size:32px;font-weight:700;color:#e9e9ea;letter-spacing:.2px;}
  .hero-copy{left:41px;top:87px;color:#f3f3f3;font-size:15.5px;line-height:20px;}
  .hero-copy p{margin-bottom:13px;text-align:justify;}
  .hero-copy .w1{width:568px;} .hero-copy .w2{width:515px;}
  .hero-copy .w3{width:485px;} .hero-copy .w4{width:412px;}

  .landscape-photo{left:522px;top:68px;width:406px;height:281px;
    clip-path:polygon(120px 0,100% 0,100% 100%,8px 100%);
    background:linear-gradient(180deg,#b9c3c6 0%,#7e9a86 28%,#4c6e3c 52%,#8e9590 72%,#3f4a3a 100%);}

  .package-note{left:525px;top:362px;width:390px;text-align:center;font-size:20px;line-height:26px;font-weight:600;color:var(--ink);}
  .package-note small{display:block;font-size:14.5px;font-weight:400;line-height:18px;}

  .investment{left:520px;top:470px;width:400px;text-align:center;font-size:23px;line-height:29px;color:var(--ink);}
  .investment strong{display:block;color:var(--orange);font-weight:700;font-size:25px;line-height:36px;}
  .value-note{left:570px;top:572px;width:298px;text-align:center;font-size:15px;line-height:20px;color:var(--ink);}

  .invite{left:41px;top:494px;width:395px;font-size:18px;line-height:23.5px;font-weight:700;color:var(--ink);}
  .contact-label{left:44px;top:597px;font-size:19px;color:var(--ink);}
  .contact-name{left:44px;top:618px;font-size:25px;font-weight:700;color:var(--orange);}
  .contact-rule{left:190px;top:601px;width:1.5px;height:50px;background:var(--ink);}
  .contact-line{left:220px;font-size:16.5px;display:flex;align-items:center;gap:10px;color:var(--ink);}
  .contact-line svg{width:18px;height:16px;}

  .section-heading{left:41px;top:686px;font-size:28px;font-weight:700;color:var(--white);}
  .bio{left:41px;top:738px;width:838px;font-size:16.4px;line-height:22px;}
  .bio p{margin-bottom:5px;}
  .credentials-title{left:41px;top:934px;font-size:16.5px;font-weight:700;}
  .credentials{list-style:none;font-size:16.5px;line-height:24.5px;}
  .credentials li{position:relative;padding-left:26px;}
  .credentials li::before{content:"•";position:absolute;left:0;font-size:12px;}
  .credentials.col-a{left:41px;top:958px;}
  .credentials.col-b{left:472px;top:934px;width:400px;}

  .brand-name{left:48px;top:1094px;font-size:36px;font-weight:400;color:var(--wordmark-grey);letter-spacing:1px;}

  .more-info{right:42px;top:1097px;text-align:right;font-size:22px;line-height:30px;color:var(--white);}
  .more-info strong{font-weight:700;}
</style>
</head>
<body>
<div class="flyer">
  <svg class="backdrop" viewBox="0 0 928 1200" aria-hidden="true">
    <rect x="640" y="0" width="288" height="68" fill="var(--orange)"/>
    <path d="M0 0 H661 L478 450 Q472 466 452 466 H0 Z" fill="var(--charcoal)"/>
    <polygon points="530,349 928,349 928,463 484,463" fill="var(--orange)"/>
    <rect x="0" y="470" width="928" height="193" fill="var(--mist)"/>
    <line x1="478" y1="468" x2="535" y2="665" stroke="var(--white)" stroke-width="10"/>
    <path d="M512 563 H928 V663 H555 Q540 663 535 648 Z" fill="var(--orange)"/>
    <rect x="0" y="698" width="928" height="370" fill="var(--mist)"/>
    <path d="M0 678 H490 Q515 678 515 703 Q515 728 490 728 H0 Z" fill="var(--orange)"/>
    <path d="M470 1085 H928 V1175 H440 Z" fill="var(--orange)"/>
    <rect x="0" y="1175" width="928" height="25" fill="var(--charcoal-dark)"/>
  </svg>

  <h1 class="abs hero-title">Northvale Executive Coaching</h1>
  <div class="abs hero-copy">
    <p class="w1">We believe great coaching is a bridge: one that enables you to see more clearly and cross the unexpected chasms; one that supports and challenges your thinking and actions to progress your significant goals.</p>
    <p class="w2">We build a creative and confidential partnership with you, one that is grounded in the science of leadership, change and coaching psychology so that practical results are an expectation and not left to chance.</p>
    <p class="w3">Our coaches are highly attuned to the human systems within which you work and live, since understanding those interconnected forces is vital to unlock movement. We build on your existing strengths and seek sustainable shifts, ones that create ripple effects of positive change.</p>
    <p class="w4">Leaders everywhere face unprecedented change, pressure, ambiguity, culture and accountability dilemmas. And yet every leader also has a different story, different terrain to navigate and different aspirations. This is where executive coaching with Northvale can create extraordinary results.</p>
  </div>

  <div class="abs landscape-photo" role="img" aria-label="Photograph of a steel truss footbridge over a river, with forest and a glacier valley behind"></div>

  <div class="abs package-note">Our coaching packages typically consist of blocks of 7 hourly sessions, conducted fortnightly<small>(with flexibility to customise).</small></div>

  <div class="abs investment">For EL2 leaders, the investment<br>in a block of<strong>7 sessions is $3400 + GST.</strong></div>
  <div class="abs value-note">This includes significant preparation and conceptualisation time before and after sessions by your coach to ensure you achieve maximum value.</div>

  <p class="abs invite">Why not explore the possibilities executive coaching offers through a no obligation initial session, ensuring the approach and the coach is a good fit for you?</p>
  <div class="abs contact-label">Contact:</div>
  <div class="abs contact-name">Tom Hallett</div>
  <div class="abs contact-rule"></div>
  <div class="abs contact-line" style="top:604px;">
    <svg viewBox="0 0 18 16" aria-hidden="true"><circle cx="9" cy="8" r="6.5" fill="none" stroke="var(--ink)" stroke-width="1.3"/><path d="M6.5 4.5 Q5 8 7 11.5 L8.5 10.5 Q7.5 8 8 5.5 Z" fill="var(--ink)"/></svg>
    <span>0400 xxx xxx</span>
  </div>
  <div class="abs contact-line" style="top:627px;">
    <svg viewBox="0 0 18 16" aria-hidden="true"><rect x="1" y="2.5" width="16" height="11" fill="none" stroke="var(--ink)" stroke-width="1.2"/><path d="M1 2.5 L9 9 L17 2.5 M1 13.5 L7 7.5 M17 13.5 L11 7.5" fill="none" stroke="var(--ink)" stroke-width="1.2"/></svg>
    <span>tom.hallett@northvaleadvisory.com</span>
  </div>

  <h2 class="abs section-heading">Meet one of our Coaches</h2>
  <div class="abs bio">
    <p>Tom Hallett leads the Executive Coaching practice for Northvale across Australia and New Zealand.</p>
    <p>He has worked at senior levels in the ACT Public Service, the Australian Public Service and in the private sector. His continuing focus over the past 20 years has been on organisational and people development. As a Masters-qualified and highly experienced executive coach, Tom’s passion lies in unlocking human potential. He has coached doctors, nurses, allied health clinicians, statisticians, scientists, educators, IT professionals, Senior managers and Executives in the APS (EL1 – SES), ACT Government (SOGC – Executive bands) and private sector.</p>
    <p>When Tom is not coaching, he is facilitating workshops and consulting to enable teams and organisations to make effective transformations.</p>
  </div>
  <h3 class="abs credentials-title">Qualifications, Accreditations, Memberships</h3>
  <ul class="abs credentials col-a">
    <li>Master of Science in Coaching Psychology</li>
    <li>Graduate Certificate in Management</li>
    <li>Certificate IV in Workplace Assessment &amp; Training</li>
    <li>Team Profile Accreditation, Meridian Insight</li>
  </ul>
  <ul class="abs credentials col-b">
    <li>Type Profile Accreditation</li>
    <li>Member, Global Coaching Guild (GCG)</li>
    <li>Member, Harbour City Coaching &amp;<br>Mentoring Alumni Association.</li>
  </ul>

  <div class="abs brand-name">Northvale Advisory</div>
  <div class="abs more-info">For details on other Northvale services<br>please visit <strong>www.northvaleadvisory.com</strong></div>
</div>
</body>
</html>
```